Business card Zottelgarten

Business card is for a self-employed dog trainer with own dog school. Name and logo of the dog school are available. Color specifications as well. The design should be classy and minimalist, but also modern. An already existing idea would be: Front: Only the logo Back: Contact data

Font styles to use
Serif
Sans Serif
Other font styles liked:
• Trajan Pro

Colors
f78f20

Requirements
Must have
• Name: Margit Wendler-Rasch Title: Dipl. Dog Trainer Contain my logo Follow my font and color preferences (see files)

```html
<!DOCTYPE html>
<html lang="de">
<head>
<meta charset="utf-8">
<title>Zottelgarten – Visitenkarte</title>
<link href="https://fonts.googleapis.com/css2?family=Cinzel:wght@400;600&family=Open+Sans:wght@400&display=swap" rel="stylesheet">
<style>
  :root {
    --stage: #1d1b1a;
    --brown: #786655;
    --brown-dark: #685646;
    --cream: #f1efec;
    --white: #ffffff;
    --orange: #f78f20;
    --ink: #6f6a66;
    --shadow: rgba(0,0,0,0.55);
  }
  * { margin: 0; padding: 0; box-sizing: border-box; }
  html, body { width: 1200px; height: 963px; overflow: hidden; }
  body {
    background: var(--stage);
    display: flex; align-items: center; justify-content: center; gap: 48px;
    font-family: "Open Sans", Arial, sans-serif;
  }
  .card {
    width: 540px; height: 315px; border-radius: 14px;
    box-shadow: 0 18px 40px var(--shadow);
    position: relative; overflow: hidden;
  }
  /* Front */
  .card--front {
    background: linear-gradient(135deg, var(--brown) 0%, var(--brown-dark) 100%);
    display: flex; flex-direction: column; align-items: center; justify-content: center;
  }
  .brand { display: flex; align-items: center; gap: 16px; }
  .brand__mark { width: 70px; height: 70px; border-radius: 50%; background: var(--cream); flex: none; }
  .brand__name {
    font-family: "Cinzel", "Times New Roman", serif; font-weight: 400;
    font-size: 34px; letter-spacing: 2px; color: var(--cream);
  }
  .brand__url {
    margin-top: 8px; font-family: "Cinzel", serif; font-size: 10px;
    letter-spacing: 6px; color: var(--cream); text-transform: uppercase;
  }
  /* Back */
  .card--back { background: var(--white); }
  .contact { position: absolute; left: 36px; top: 44px; color: var(--ink); }
  .contact__name {
    font-family: "Cinzel", "Times New Roman", serif; font-weight: 600;
    font-size: 19px; color: var(--orange); letter-spacing: 0.5px;
  }
  .contact__title, .contact__address { font-size: 13px; line-height: 19px; }
  .contact__title { margin-top: 4px; }
  .contact__list { list-style: none; margin-top: 10px; font-size: 13px; line-height: 20px; }
  .contact__list li { display: flex; align-items: center; gap: 10px; }
  .contact__list svg { width: 11px; height: 11px; flex: none; }
  .rule { position: absolute; left: 210px; right: 32px; top: 78px; height: 1.5px; background: var(--orange); }
  .card--back .brand { position: absolute; right: 36px; bottom: 54px; flex-direction: column; align-items: flex-end; gap: 10px; }
  .card--back .brand__mark { width: 62px; height: 62px; background: var(--brown); }
  .card--back .brand__name { font-size: 24px; color: var(--brown); letter-spacing: 1.5px; }
  .card--back .brand__url { position: absolute; right: 36px; bottom: 38px; font-size: 8px; letter-spacing: 4px; color: var(--brown); margin: 0; }
</style>
</head>
<body>
  <section class="card card--front">
    <div class="brand">
      <span class="brand__mark"></span>
      <span class="brand__name">ZOTTELGARTEN</span>
    </div>
    <p class="brand__url">www.zottelgarten.ch</p>
  </section>

  <section class="card card--back">
    <div class="contact">
      <h1 class="contact__name">MARGIT WENDLER-RASCH</h1>
      <p class="contact__title">Dipl. Dog Trainer</p>
      <p class="contact__address">Lindenweg 12,<br>Uster</p>
      <ul class="contact__list">
        <li><svg viewBox="0 0 12 12"><path d="M3 1l2 2.5-1.2 1.3a7 7 0 0 0 3.4 3.4L8.5 7 11 9l-1 2C5.5 11 1 6.5 1 2z" fill="var(--orange)"/></svg>(123) 456-7890</li>
        <li><svg viewBox="0 0 12 12"><rect x="1" y="2.5" width="10" height="7" fill="none" stroke="var(--orange)" stroke-width="1.2"/><path d="M1 2.5l5 4 5-4" fill="none" stroke="var(--orange)" stroke-width="1.2"/></svg>info@zottelgarten.ch</li>
        <li><svg viewBox="0 0 12 12"><circle cx="6" cy="6" r="4.8" fill="none" stroke="var(--orange)" stroke-width="1.2"/><path d="M1.2 6h9.6M6 1.2c-2.4 3-2.4 6.6 0 9.6M6 1.2c2.4 3 2.4 6.6 0 9.6" fill="none" stroke="var(--orange)" stroke-width="0.9"/></svg>www.zottelgarten.ch</li>
      </ul>
    </div>
    <div class="rule"></div>
    <div class="brand">
      <span class="brand__mark"></span>
      <span class="brand__name">ZOTTELGARTEN</span>
    </div>
    <p class="brand__url">www.zottelgarten.ch</p>
  </section>
</body>
</html>
```